Create a Flyer for a Darts Tournament

We need a Flyer for a Darts Tournament that is going to be organized by our darts department (logo attached). The name of the tournament is "3. KLW Dartsturnier". The Flyer should look modern, professional and in a way that everyone can see at the first impression that is has to do with dart sports. The logo of our department should be on the flyer as well. On the flyer we need an area where we can place some informations regarding the tournament (bullet points) etc. And a area where we can place informations regarding the registration progress (e.g. "Registration via E-Mail". Should fit well to our logo.

Target Market(s)

Darts Players for the Tournament

Font styles to use
Serif

Colors

Designer to choose colors to be used in the design.

Requirements
Must have
• Name of the Tournament, our Logo, place for some tournament details, link to our registration page (besucher.tv-hallwitz.de). Should

```html
<!DOCTYPE html>
<html lang="de">
<head>
<meta charset="utf-8">
<title>3. KLW Dartsturnier</title>
<link href="https://fonts.googleapis.com/css2?family=Exo+2:wght@500;600;700;800&display=swap" rel="stylesheet">
<style>
  :root {
    --night: #05080f;
    --navy: #0a2a66;
    --deep-blue: #0b4fa3;
    --blue: #0f7fd6;
    --sky: #22a8ec;
    --white: #ffffff;
    --silver-light: #f2f4f6;
    --silver-dark: #a9afb6;
    --pill: #0c3270;
  }
  * { margin: 0; padding: 0; box-sizing: border-box; }
  html, body { width: 1023px; height: 1200px; overflow: hidden; background: var(--night); }
  .flyer {
    position: relative; width: 1023px; height: 1200px; overflow: hidden;
    font-family: "Exo 2", sans-serif; color: var(--white);
    background: radial-gradient(circle at 90% 30%, #123a7a 0%, #0a1a3a 25%, var(--night) 55%);
  }
  .photo-dartboard {
    position: absolute; left: 0; top: 0; width: 620px; height: 760px;
    background: radial-gradient(ellipse at 30% 40%, #cfd2d6 0%, #8e9297 30%, #3b3e43 60%, rgba(5,8,15,0) 85%);
  }
  .club-mark {
    position: absolute; left: 721px; top: 150px; width: 221px;
    display: flex; align-items: center; justify-content: center; gap: 12px;
  }
  .club-mark .dot { width: 26px; height: 26px; border-radius: 50%; background: var(--sky); }
  .club-mark .name { font-weight: 800; font-size: 40px; color: var(--white); letter-spacing: 1px; }
  .title-block { position: absolute; left: 561px; top: 358px; width: 393px; height: 184px; }
  .title-block svg { position: absolute; inset: 0; }
  .title-main {
    position: absolute; left: 0; top: 8px; width: 100%; text-align: center;
    font-weight: 800; font-size: 92px; line-height: 100px; color: var(--white);
    text-shadow: 3px 3px 0 var(--navy);
  }
  .title-sub {
    position: absolute; left: 0; top: 114px; width: 100%; text-align: center;
    font-weight: 700; font-size: 46px; line-height: 56px; color: var(--navy);
  }
  .info-panel { position: absolute; left: 0; top: 0; }
  .date-ribbon { position: absolute; left: 213px; top: 657px; width: 595px; height: 74px; }
  .date-ribbon svg { position: absolute; inset: 0; }
  .date-ribbon .date {
    position: absolute; left: 0; top: 0; width: 100%; height: 66px; line-height: 66px;
    text-align: center; font-weight: 700; font-size: 40px; color: var(--navy);
  }
  .details { position: absolute; left: 211px; top: 748px; width: 600px; list-style: none; }
  .details li {
    height: 46px; line-height: 46px; text-align: center;
    font-weight: 600; font-size: 22px; margin: 0 auto;
    border-bottom: 1.5px solid rgba(255,255,255,0.85);
  }
  .details li:nth-child(1) { width: 500px; }
  .details li:nth-child(2) { width: 500px; }
  .details li:nth-child(3) { width: 450px; }
  .details li:nth-child(4) { width: 400px; }
  .details li:nth-child(5) { width: 400px; }
  .details li:nth-child(6) { width: 400px; }
  .details li:last-child { border-bottom: none; }
  .registration {
    position: absolute; left: 214px; top: 1091px; width: 629px; height: 46px;
    border-radius: 23px; background: var(--pill);
    display: flex; align-items: center; justify-content: center; gap: 14px;
    font-weight: 600; font-size: 28px;
  }
  .registration .mail-icon {
    width: 42px; height: 42px; border-radius: 50%; background: var(--white);
    display: flex; align-items: center; justify-content: center;
  }
</style>
</head>
<body>
<div class="flyer">
  <div class="photo-dartboard" role="img" aria-label="Foto einer Dartscheibe mit vier roten und gelben Pfeilen im Bullseye"></div>

  <div class="club-mark">
    <span class="dot"></span>
    <span class="name">KLW Darts</span>
  </div>

  <div class="title-block">
    <svg width="393" height="184" viewBox="0 0 393 184">
      <defs>
        <linearGradient id="titleBlue" x1="0" y1="0" x2="0" y2="1">
          <stop offset="0" stop-color="#1c9be6"/>
          <stop offset="1" stop-color="#0b5fc0"/>
        </linearGradient>
      </defs>
      <polygon points="22,2 392,2 374,112 40,112" fill="url(#titleBlue)" stroke="#c8ccd2" stroke-width="3"/>
      <polygon points="14,112 380,112 364,181 30,181" fill="#0b4fa3"/>
      <polygon points="18,114 376,114 362,174 28,174" fill="#ffffff"/>
    </svg>
    <div class="title-main">3. KLW</div>
    <div class="title-sub">Dartsturnier</div>
  </div>

  <svg class="info-panel" width="1023" height="1200" viewBox="0 0 1023 1200">
    <defs>
      <linearGradient id="panelBlue" x1="0" y1="0" x2="1" y2="1">
        <stop offset="0" stop-color="#2bb3f0"/>
        <stop offset="0.5" stop-color="#1996e0"/>
        <stop offset="1" stop-color="#0f7ad0"/>
      </linearGradient>
      <linearGradient id="silver" x1="0" y1="0" x2="0" y2="1">
        <stop offset="0" stop-color="#ffffff"/>
        <stop offset="0.5" stop-color="#e4e7ea"/>
        <stop offset="1" stop-color="#a9afb6"/>
      </linearGradient>
    </defs>
    <path d="M60,592 Q220,570 330,582 Q440,595 511,580 Q560,566 640,580 Q780,572 906,562 L983,825 Q880,930 983,1037 L940,1200 L109,1200 L31,1037 Q130,930 31,825 Z"
          fill="url(#panelBlue)" stroke="#0b4fa3" stroke-width="6"/>
    <g transform="translate(213,657)">
      <polygon points="0,0 595,0 570,36 595,74 0,74 25,36" fill="#0b4fa3"/>
      <polygon points="6,0 589,0 566,33 589,66 6,66 29,33" fill="url(#silver)"/>
    </g>
  </svg>

  <div class="date-ribbon"><div class="date">Samstag, 25.01.2025</div></div>

  <ul class="details">
    <li>Einlass 16:00 Uhr / Turnierbeginn 17:00 Uhr</li>
    <li>Steel-Darts-Hobbyturnier (keine Ligaspieler)</li>
    <li>SVZ in 54321 Hallwitz-Nordheim</li>
    <li>Maximal 48 Teilnehmer</li>
    <li>Gruppenphase 301 | DO | BO3</li>
    <li>KO-Phase 501 | DO | BO5</li>
    <li>Infos: darts.tv-hallwitz.de</li>
  </ul>

  <div class="registration">
    <span>Anmeldung:</span>
    <span class="mail-icon">
      <svg width="24" height="18" viewBox="0 0 24 18">
        <rect x="1" y="1" width="22" height="16" rx="2" fill="none" stroke="#0c3270" stroke-width="2"/>
        <polyline points="1,2 12,10 23,2" fill="none" stroke="#0c3270" stroke-width="2"/>
      </svg>
    </span>
    <span>besucher.tv-hallwitz.de</span>
  </div>
</div>
</body>
</html>
```